Marlow Fenn Grill buffet and restaurant sold by the pound

I need something cool but informative and with all my day to day menu and catering . I want something with a organic feel but that works well with my branding so far . Using my logo and Brazilian colors.
Menu
Lunch-Dinner
Make your Combination Plate(Salads, Hot Dishes and Churrasco Meats) Sold by the Pound!!!
Salads + Hot Dishes (Buffet only) $8.65 per/Lb
Churrasco Meats+Hot Dishes+Salads $9.85 per/Lb
Churrasco Meats ( Only Meat) $15.95 per/Lb

Drinks

Guarana/Diet $2.50 Fruit Juice(especials) $4.50
Zesto/Diet $2.00 Vitamina (Fruit+Milk) $5.00 Flicker/Diet $2.00 Ice Tea/ Diet $2.00

Breakfast
7am-10am
Frittata $8.00

French Baguette Sandwich $8.00
Build your own
Cheese(Havarti/mozzarella)/Tomatoes/onions/bacon/lettuce
Beef/Chicken / Lombinho( Pork file)

Dessert ( Specials) $?

Catering Menu
*Pork chops stuffed with Garlic $35.00 (serves 5)
* Chicken Pot Pie Medium $60 (serves 8)
Large good for 15 people $110
*Chicken on Mango Sauce $34(serves 5)
*Eggplant Lasagna with banana Medium$30( serves 6)
Large $60 (serves 12)
*Try-tip stuffed with Bacon $53 (serves 5)
* Bacalhau ( dried cod fish) Chef style Medium $60( serve 6)
Large $120 (serves 14)
*Passion Fruit Mousse 320 ounce $25
*Strawberry Truffle Pie 320 ounce $30

Restaurant

• Menu
• Lunch-Dinner
• Make your Combination Plate(Salads, Hot Dishes and Churrasco Meats) Sold by the Pound!!!
• Salads + Hot Dishes (Buffet only) $8.65 per/Lb
• Churrasco Meats+Hot Dishes+Salads $9.85 per/Lb
• Churrasco Meats ( Only Meat) $15.95 per/Lb
• Drinks
• Guarana/Diet $2.50 Fruit Juice(specials menu) $4.50
• Zesto/Diet $2.00 Vitamin (Fruit+Milk) $5.00 Flicker/Diet $2.00 Ice Tea/ Diet $2.00
• Breakfast
• 7am-10am
• Frittata $8.00
• French Baguette Sandwich $8.00
• Build your own
• Cheese(Havarti/mozzarella)/Tomatoes/onions/bacon/lettuce
• Beef/Chicken / Lombinho( Pork file)
• Dessert ( Specials Menu) $?
• Catering Menu
• *Pork chops stuffed with Garlic serves 4-5 $35.00
• * Chicken Pot Pie serves 7-8 $60
• serves 14-15 $110
• *Chicken on Mango Sauce serves 4-5 $34
• *Eggplant Lasagna with banana serves 5-6 $30
• serves 12 - 13 $60
• *Try-tip stuffed with Bacon serves 4-5 $53
• * Bacalhau ( dried cod fish) Chef style serves 5-6 $60
• serves 14-15 $120
• *Passion Fruit Mousse 320 ounce $25
• *Strawberry Truffle Pie 320 ounce $30

```html
<!DOCTYPE html>
<html lang="en">
<head>
<meta charset="utf-8">
<title>Marlow Fenn Grill – Menu</title>
<link rel="stylesheet" href="https://fonts.googleapis.com/css2?family=Kreon:wght@500;700&family=Poppins:wght@500&family=Roboto+Condensed:wght@400;700&display=swap">
<style>
:root{
  --wood-dark:#4a3322;
  --wood-mid:#7a5a3f;
  --parchment:#e9dcc3;
  --parchment-light:#f1e7d3;
  --leaf:#4f8f32;
  --teal:#2c7088;
  --ochre:#a87a1d;
  --plank:#d9cbb3;
  --plank-line:#b9a78c;
  --ink:#1d1a17;
  --white:#ffffff;
  --logo:#1e5570;
  --footer:#2a2420;
}
*{box-sizing:border-box;margin:0;padding:0}
html,body{width:849px;height:1200px;overflow:hidden}
body{position:relative;background:linear-gradient(160deg,var(--wood-mid),var(--wood-dark));font-family:"Poppins",sans-serif;color:var(--ink)}
.sheet{position:absolute;left:24px;top:72px;width:804px;height:1088px;background:linear-gradient(180deg,var(--parchment-light),var(--parchment));border:5px solid var(--leaf)}
.sheet-arch{position:absolute;left:194px;top:20px;width:460px;height:70px;background:var(--parchment-light);border-radius:230px 230px 0 0}
.foliage{position:absolute;top:0;height:60px;width:200px;background:linear-gradient(180deg,#3f7a2a,rgba(63,122,42,0))}
.foliage.left{left:0}.foliage.right{right:0}
.brand{position:absolute;left:0;width:849px;top:104px;display:flex;justify-content:center;align-items:center;gap:14px}
.brand-dot{width:22px;height:22px;border-radius:50%;background:var(--logo)}
.brand-name{font-family:"Kreon",serif;font-weight:700;font-size:46px;color:var(--logo)}
.card{position:absolute;border-radius:10px}
.card-title{font-family:"Kreon",serif;font-weight:700;color:var(--white);text-align:center;line-height:1}
.board{position:absolute;background:repeating-linear-gradient(180deg,var(--plank) 0 24px,var(--plank-line) 24px 25px);border-radius:8px}
.row{display:flex;text-transform:uppercase;white-space:nowrap}
.row .price{margin-left:auto}
.lunch{left:54px;top:214px;width:750px;height:260px;background:var(--teal)}
.lunch .card-title{font-size:40px;margin-top:16px}
.lunch .sub{font-family:"Roboto Condensed",sans-serif;color:var(--white);font-size:18px;text-align:center;line-height:24px;margin-top:10px}
.lunch .board{left:10px;top:120px;width:732px;height:130px;padding:10px 16px}
.lunch .row{font-size:20px;line-height:36px}
.lunch .row .name{width:478px}
.lunch .row .price{margin-left:0}
.drinks{left:54px;top:488px;width:358px;height:246px;background:var(--ochre)}
.drinks .card-title{font-size:38px;margin-top:14px}
.drinks .board{left:10px;top:62px;width:338px;height:174px;padding:8px 10px}
.drinks .row{font-size:19px;line-height:26.4px}
.breakfast{left:424px;top:488px;width:380px;height:246px;background:var(--ochre)}
.breakfast .card-title{font-size:38px;margin-top:14px}
.breakfast .card-title small{font-size:28px}
.breakfast .board{left:10px;top:70px;width:362px;height:166px;padding:6px 12px}
.breakfast .row{font-size:19px;line-height:26.4px}
.breakfast .build{font-family:"Roboto Condensed",sans-serif;font-weight:700;font-size:15px;text-align:center;line-height:23px}
.catering{left:270px;top:749px;width:534px;height:399px;background:var(--leaf)}
.catering .card-title{font-size:40px;margin-top:14px}
.catering .board{left:10px;top:66px;width:514px;height:324px;padding:4px 10px 4px 22px}
.catering .row{font-size:15.5px;line-height:22.8px}
.catering .row.size{padding-left:12px}
.catering .row .price{margin-left:0;position:absolute;left:422px}
.catering .row{position:relative}
.landmark-photo{position:absolute;left:0;top:720px;width:270px;height:440px;background:linear-gradient(180deg,rgba(233,220,195,0) 0%,#c9a46a 35%,#8a6a3a 70%,#3d3a22 100%)}
.footer{position:absolute;left:0;top:1160px;width:849px;height:40px;background:var(--footer);color:var(--white);font-family:"Kreon",serif;font-weight:500;font-size:23px;display:flex;align-items:center;justify-content:space-between;padding:0 42px 0 58px}
.phone{display:flex;align-items:center;gap:8px}
</style>
</head>
<body>
<div class="sheet"></div>
<div class="sheet-arch"></div>
<div class="foliage left" role="img" aria-label="Hanging green leaves"></div>
<div class="foliage right" role="img" aria-label="Hanging green leaves"></div>

<div class="brand"><span class="brand-dot"></span><span class="brand-name">Marlow Fenn Grill</span></div>

<section class="card lunch">
  <h1 class="card-title">Menu Lunch-Dinner</h1>
  <p class="sub">Make your Combination Plate (Salads, Hot Dishes and Churrasco Meats)<br>Sold by the Pound!!!</p>
  <div class="board">
    <div class="row"><span class="name">Salads + Hot Dishes (Buffet Only)</span><span class="price">$8.65 per/lb</span></div>
    <div class="row"><span class="name">Churrasco Meats+Hot Dishes+Salads</span><span class="price">$9.85 per/lb</span></div>
    <div class="row"><span class="name">Churrasco Meats ( Only Meat)</span><span class="price">$15.95 per/lb</span></div>
  </div>
</section>

<section class="card drinks">
  <h2 class="card-title">Drinks</h2>
  <div class="board">
    <div class="row"><span>Guarana/Diet</span><span class="price">$2.50</span></div>
    <div class="row"><span>Fruit Juice(Especials)</span><span class="price">$4.50</span></div>
    <div class="row"><span>Zesto/Diet</span><span class="price">$2.00</span></div>
    <div class="row"><span>Vitamina (Fruit+Milk)</span><span class="price">$5.00</span></div>
    <div class="row"><span>Flicker/Diet</span><span class="price">$2.00</span></div>
    <div class="row"><span>Ice Tea/ Diet</span><span class="price">$2.00</span></div>
  </div>
</section>

<section class="card breakfast">
  <h2 class="card-title">Breakfast <small>7am-10 am</small></h2>
  <div class="board">
    <div class="row"><span>Frittata</span><span class="price">$8.00</span></div>
    <div class="row"><span>French Baguette</span><span class="price">$8.00</span></div>
    <div class="row"><span>Sandwich</span></div>
    <p class="build">Build your own<br>Cheese(Havarti/mozzarella)/Tomatoes/onions/<br>bacon/lettuce/Beef/Chicken / Lombinho( Pork file)</p>
  </div>
</section>

<div class="landmark-photo" role="img" aria-label="Photo of a hilltop statue overlooking the city at sunset"></div>

<section class="card catering">
  <h2 class="card-title">CATERING MENU</h2>
  <div class="board">
    <div class="row"><span>* Pork chops stuffed with garlic (serves 5)</span><span class="price">$35.00</span></div>
    <div class="row"><span>* Chicken on mango sauce (serves 5)</span><span class="price">$34</span></div>
    <div class="row"><span>* Try-tip stuffed with bacon (serves 5)</span><span class="price">$53</span></div>
    <div class="row"><span>* Chicken pot pie</span></div>
    <div class="row size"><span>(Serves 8)</span><span class="price">$60</span></div>
    <div class="row size"><span>(Serves 15)</span><span class="price">$110</span></div>
    <div class="row"><span>* Eggplant lasagna with banana</span></div>
    <div class="row size"><span>(Serves 6)</span><span class="price">$30</span></div>
    <div class="row size"><span>(Serves 12)</span><span class="price">$60</span></div>
    <div class="row"><span>* Bacalhau ( dried cod fish) chef style</span></div>
    <div class="row size"><span>(Serve 6)</span><span class="price">$60</span></div>
    <div class="row size"><span>(Serves 14)</span><span class="price">$120</span></div>
    <div class="row"><span>* Passion fruit mousse 320 ounce</span><span class="price">$25</span></div>
    <div class="row"><span>* Strawberry truffle pie 320 ounce</span><span class="price">$30</span></div>
  </div>
</section>

<footer class="footer">
  <span class="address">1480 Willow Crest Ave, Ste. E, Dunmore, CA 90000</span>
  <span class="phone">
    <svg width="26" height="26" viewBox="0 0 26 26" aria-hidden="true"><circle cx="13" cy="13" r="13" fill="#fff"/><path d="M9 6.5l2.4 3.6-1.5 1.6c.8 1.8 2.2 3.2 4 4l1.6-1.5 3.6 2.4-1.3 2.6c-5.5-.4-10.2-5.1-10.6-10.6z" fill="#2a2420"/></svg>
    555 014-2278
  </span>
</footer>
</body>
</html>
```